Willowmere Spa and Beauty Ltd. (Name of business)

I need a business card designed for this new company based out of Toronto Ontario. We specialize in Eyelash Extensions, Manicures and Pedicures, body waxing, massages, laser hair removal and anti-wrinkle treatments. Also offer a variety of products for sale, such as skin cream serums, collagen gel, eye cream, etc. It is a safe relaxing and non-judgemental environnment. Clients are welcome to come be pampered for the half or full day. Many service packages to choose from.

Open 7days per week from 8am to 8pm.

Marissa Thornbury
Spa Facilitator
Willowmere Spa and Beauty Ltd.
7200 Calder Ave; Suite 1400
Toronto ON K8P 2W7

OFFICE: 416.739.4100
FAX: 416.739.4101
CELL: 416.582.6074
EMAIL: marissa.thornbury@willowmerespa.example

Target Market(s)

Target market is primarily female ranging from 16 years old to 50 years old.

Industry/Entity Type

Business

Contact Information for Business Card

Marissa Thornbury
Spa Facilitator
7200 Calder Ave; Suite 1400
Toronto ON K8P 2W7

OFFICE: 416.739.4100
FAX: 416.739.4101
CELL: 416.582.6074

Logo Text

I dont have a logo yet. I would like it simple but sophisticated and modern.

Font styles to use
Serif

Requirements
Must have
• all pertinent details such as company name, logo, name and contact information, services that are offered, including package rates
Nice to have
• Company name and logo prominent. A card that is neat and the information such as address, phone number, fax, email, etc is not too crowded but laid out in an easy to read format.
• Possibly on the back of card - some of the services offered could be listed, as well as professional cream lotions and serums. Hours of operation etc.

```html
<!DOCTYPE html>
<html lang="en">
<head>
<meta charset="utf-8">
<title>Willowmere Spa and Beauty Ltd. – Business Card</title>
<link rel="stylesheet" href="https://fonts.googleapis.com/css2?family=Lato:wght@300;400;700&display=swap">
<style>
  :root {
    --pink: #d65aa4;
    --ink: #3a3a3a;
    --muted: #555555;
    --paper: #ffffff;
    --slate: #4a4a4a;
    --slate-dark: #3c3c3c;
    --slate-text: #c9c9c9;
    --backdrop: #e9e9ec;
    --photo-light: #efe9df;
    --photo-warm: #d9c3a8;
  }
  * { box-sizing: border-box; margin: 0; padding: 0; }
  html, body {
    width: 1200px; height: 1000px; overflow: hidden;
    background: var(--backdrop);
    font-family: "Lato", Arial, sans-serif;
  }
  .canvas { position: relative; width: 1200px; height: 1000px; }
  .card {
    position: absolute; top: 150px;
    width: 400px; height: 700px;
    overflow: hidden;
    box-shadow: 0 10px 30px rgba(0,0,0,0.18);
  }
  /* Front */
  .card--front { left: 180px; background: var(--paper); }
  .front-hero { position: absolute; top: 0; left: 0; width: 400px; height: 340px; }
  .holder { position: absolute; left: 40px; top: 352px; }
  .holder-name {
    color: var(--pink); font-weight: 700; font-size: 32px; letter-spacing: 0.3px; line-height: 40px;
  }
  .holder-title {
    color: var(--ink); font-weight: 400; font-size: 18px; margin-top: 2px;
  }
  .contact-list { position: absolute; left: 40px; top: 452px; list-style: none; }
  .contact-item {
    display: flex; align-items: flex-start; height: 34px;
    color: var(--muted); font-size: 19px; font-weight: 300; letter-spacing: 0.4px; line-height: 26px;
  }
  .contact-item--email { font-size: 15.5px; letter-spacing: 0.2px; }
  .contact-item--address { height: auto; line-height: 24px; font-size: 17px; }
  .contact-icon { width: 26px; height: 26px; margin-right: 16px; flex: none; }
  .front-band {
    position: absolute; left: 0; bottom: 0; width: 100%; height: 26px; background: var(--pink);
  }
  /* Back */
  .card--back {
    left: 620px;
    background: radial-gradient(ellipse at 55% 40%, var(--slate) 0%, var(--slate-dark) 100%);
  }
  .brand-band {
    position: absolute; left: 0; top: 150px; width: 100%; height: 64px;
    background: var(--pink);
    display: flex; align-items: center; padding-left: 30px;
  }
  .brand-name { color: var(--paper); font-weight: 300; font-size: 19px; letter-spacing: 0.6px; }
  .services {
    position: absolute; left: 30px; top: 340px;
    border-left: 4px solid var(--pink);
    padding-left: 18px; list-style: none;
  }
  .service-line {
    color: var(--slate-text); font-weight: 300; font-size: 15px; line-height: 26px; letter-spacing: 0.3px;
  }
</style>
</head>
<body>
<main class="canvas">

  <section class="card card--front" aria-label="Business card front">
    <svg class="front-hero" viewBox="0 0 400 340">
      <defs>
        <linearGradient id="heroTone" x1="0" y1="0" x2="1" y2="1">
          <stop offset="0" stop-color="#efe9df"/>
          <stop offset="1" stop-color="#d9c3a8"/>
        </linearGradient>
      </defs>
      <path role="img" aria-label="Photo of a relaxed spa guest resting on a towel"
            d="M0 0 H400 V150 Q350 300 0 292 Z" fill="url(#heroTone)"/>
      <path class="hero-swoosh" d="M0 292 Q350 300 400 150 V172 Q350 332 0 322 Z" fill="#d65aa4"/>
    </svg>

    <div class="holder">
      <h1 class="holder-name">Marissa Thornbury</h1>
      <p class="holder-title">Spa Facilitator</p>
    </div>

    <ul class="contact-list">
      <li class="contact-item">
        <svg class="contact-icon" viewBox="0 0 26 26" aria-label="Cell"><rect x="7" y="2" width="12" height="22" rx="2" fill="none" stroke="#666" stroke-width="1.6"/><line x1="11" y1="20" x2="15" y2="20" stroke="#666" stroke-width="1.6"/></svg>
        <span>416 582 6074</span>
      </li>
      <li class="contact-item">
        <svg class="contact-icon" viewBox="0 0 26 26" aria-label="Office"><path d="M7 4 L10 4 L12 9 L9.5 11 Q11.5 15.5 15 17 L17 14.5 L22 16.5 L22 19.5 Q21 22 18 22 Q6 20 4 8 Q4 5 7 4 Z" fill="none" stroke="#666" stroke-width="1.6" stroke-linejoin="round"/></svg>
        <span>416 739 4100</span>
      </li>
      <li class="contact-item">
        <svg class="contact-icon" viewBox="0 0 26 26" aria-label="Fax"><rect x="7" y="3" width="12" height="7" fill="none" stroke="#666" stroke-width="1.6"/><rect x="3" y="10" width="20" height="10" rx="1.5" fill="none" stroke="#666" stroke-width="1.6"/><rect x="7" y="16" width="12" height="7" fill="#fff" stroke="#666" stroke-width="1.6"/></svg>
        <span>416 739 4101</span>
      </li>
      <li class="contact-item contact-item--email">
        <svg class="contact-icon" viewBox="0 0 26 26" aria-label="Email"><rect x="3" y="6" width="20" height="14" fill="none" stroke="#666" stroke-width="1.6"/><path d="M3 6 L13 14 L23 6" fill="none" stroke="#666" stroke-width="1.6"/></svg>
        <span>marissa.thornbury@willowmerespa.example</span>
      </li>
      <li class="contact-item contact-item--address">
        <svg class="contact-icon" viewBox="0 0 26 26" aria-label="Address"><path d="M13 23 Q5 14 5 10 A8 8 0 0 1 21 10 Q21 14 13 23 Z" fill="none" stroke="#666" stroke-width="1.6"/><circle cx="13" cy="10" r="3" fill="none" stroke="#666" stroke-width="1.6"/></svg>
        <span>7200 Calder Ave; Suite 1400<br>Toronto On K8P 2W7</span>
      </li>
    </ul>

    <div class="front-band"></div>
  </section>

  <section class="card card--back" aria-label="Business card back">
    <div class="brand-band">
      <p class="brand-name">Willowmere Spa and Beauty Ltd</p>
    </div>
    <ul class="services">
      <li class="service-line">Manicures and Pedicures | body waxing</li>
      <li class="service-line">Removal and anti-wrinkle treatments | laser hair</li>
      <li class="service-line">Eyelash Extensions | massages</li>
    </ul>
  </section>

</main>
</body>
</html>
```